Window Tinting Website Design

We are working with a Window Tinting company in California. They do commercial, residential, and automotive tint.

Some websites for inspiration:
https://www.velofilmz.com/
https://www.tkglossbay.com/
https://orbishadez.com/

Thank you for taking the time to consider designing a website for us. We are web developers based in Stockton, CA, USA. Most of our projects go through the same process. Understanding this process may help you win a project with us. We custom-code all of our websites in-house. We don’t have any requirements as to what tools you use for your design, but we ask that you follow these guidelines.

IMAGES:
If you use any images or icons in the design, we ask that you have a link to the asset so we can purchase the image/icon. Most of the designs we submit do not have the customer’s images on them unless they have some great images. Be creative; show us the feeling you are trying to portray with your image choices. Use any royalty-free site you choose. We subscribe to Brellix and mainly use their images, but we can purchase images outside of Brellix. PLEASE NOTE: we will not submit designs to clients with watermarks on the images.

FONTS:
We ask that you identify the fonts you’re using in the design. This can be done in a message if you want. We typically use Tarvo Fonts and Brellix Fonts.

CONTENT:
We're always open to different content and ideas. We often submit designs with stock images so the client can see our vision. We typically take pictures after the website launch to use their images with our vision. Lorem Ipsum is fine for paragraphs, but we ask that you make the Headers with correct English. We want to be able to show the vision and identify the sections of the website.

INSPIRATION:
We typically add a couple of links in the brief of websites we like to help you get started in your design.

REVISIONS:
We do not often ask for revisions of the designs unless we see something in the design that may not appeal to the client. If there are slight changes that we want to make, we do that in the development process.

FEEDBACK:
We rarely give feedback on designs during the design process. We are working on many website projects and do not have the time to provide feedback. We usually respond if your request is well thought out and asks specific questions, but a note asking “feedback, please” usually goes unanswered.

```html
<!DOCTYPE html>
<html lang="en">
<head>
<meta charset="utf-8">
<title>Sunline Tint — Window Tinting</title>
<link href="https://fonts.googleapis.com/css2?family=Playfair+Display:ital,wght@1,700&family=Arimo:wght@400;700&family=Inter:wght@700;800&display=swap" rel="stylesheet">
<style>
:root{
  --bg:#000;
  --red:#d3202f;
  --white:#fff;
  --muted:#8a8a8a;
  --soft:#cfcfcf;
  --rule:#2a2a2a;
  --gold:#f1c21b;
}
*{margin:0;padding:0;box-sizing:border-box}
html,body{width:1200px;height:3432px;overflow:hidden;background:var(--bg)}
body{position:relative;font-family:"Arimo",Arial,sans-serif;color:var(--white)}
.abs{position:absolute}
.serif{font-family:"Playfair Display",Georgia,serif;font-style:italic;font-weight:700;text-transform:uppercase}
.brand{font-family:"Arimo",Arial,sans-serif;font-weight:700;color:var(--white);font-size:16px;display:flex;align-items:center;gap:8px;letter-spacing:.5px}
.brand i{display:block;width:16px;height:16px;border-radius:50%;background:var(--red)}
/* nav */
.nav{left:393px;top:20px;display:flex;gap:0;font-size:12.5px}
.nav a{color:var(--white);text-decoration:none;position:absolute;white-space:nowrap}
.call{left:956px;top:0;width:75px;height:77px;background:var(--red);border-radius:0 0 8px 8px;display:flex;align-items:center;justify-content:center;box-shadow:0 3px 0 #fff inset}
/* hero */
.hero-photo{left:640px;top:69px;width:560px;height:444px;background:radial-gradient(ellipse at 70% 40%,#6b5a55 0%,#3a3a40 35%,#16161a 70%,#000 100%)}
.eyebrow{left:169px;top:159px;font-size:13px;letter-spacing:1px;display:flex;align-items:center;gap:14px}
.eyebrow span{display:block;width:46px;height:2px;background:var(--red)}
.hero-title{left:169px;top:184px;font-size:39px;line-height:50px}
.hero-text{left:169px;top:298px;width:470px;font-size:13px;line-height:21px;letter-spacing:.4px;color:#e8e8e8}
.btn-red{left:169px;top:382px;width:196px;height:39px;background:var(--red);border-radius:3px;font-size:13px;font-weight:700;letter-spacing:1px;display:flex;align-items:center;justify-content:center}
.ghost{font-family:"Inter",Arial,sans-serif;font-weight:800;color:transparent;-webkit-text-stroke:1.5px #2b2b2b;line-height:1;white-space:nowrap}
/* stats */
.stat-num{top:591px;font-family:"Inter",Arial,sans-serif;font-weight:700;font-size:42px}
.stat-label{top:676px;font-size:11.5px;line-height:18px;letter-spacing:.6px;color:var(--muted)}
/* cards */
.card{width:418px;height:314px;overflow:hidden}
.card .photo{position:absolute;inset:0}
.card .shade{position:absolute;inset:0;background:linear-gradient(180deg,rgba(0,0,0,0) 35%,rgba(0,0,0,.85) 85%)}
.card h3{position:absolute;left:25px;top:208px;font-size:17px;letter-spacing:.5px}
.card p{position:absolute;left:25px;top:239px;width:330px;font-size:11.5px;line-height:18px;letter-spacing:.4px}
.card .more{position:absolute;left:25px;top:290px;font-size:10px;color:var(--red)}
/* section */
.section-title{font-size:27px;letter-spacing:.5px}
.video{left:169px;top:1638px;width:862px;height:381px;border-radius:14px;background:linear-gradient(90deg,#2d3036 0%,#1e2126 45%,#15171b 100%)}
.play{left:564px;top:1793px;width:73px;height:73px;background:var(--red);border-radius:8px;display:flex;align-items:center;justify-content:center}
/* features */
.frame{left:152px;top:2138px;width:389px;height:473px;background:var(--red);border-radius:18px 18px 0 18px}
.feat-photo{left:176px;top:2165px;width:391px;height:472px;border-radius:14px;background:linear-gradient(180deg,#3b1a1e 0%,#26303a 40%,#6b5a48 62%,#0f4c55 100%)}
.feat .icon{position:absolute;left:0;top:0;width:58px;height:58px;border-radius:50%;background:var(--red);display:flex;align-items:center;justify-content:center}
.feat .num{position:absolute;left:120px;top:2px;font-family:"Inter",Arial,sans-serif;font-weight:700;font-size:42px;color:transparent;-webkit-text-stroke:1.2px #8a8a8a}
.feat h4{position:absolute;left:0;top:78px;font-size:16.5px;white-space:nowrap;letter-spacing:.4px}
.feat p{position:absolute;left:0;top:110px;width:175px;font-size:11.5px;line-height:21px;letter-spacing:.6px;color:var(--muted)}
/* reviews */
.review-card{left:627px;top:2751px;width:403px;height:275px;border:2px solid var(--red);border-radius:4px}
.btn-line{left:169px;top:2954px;width:110px;height:37px;border:1.5px solid var(--red);border-radius:3px;font-size:13px;font-weight:700;letter-spacing:1px;display:flex;align-items:center;justify-content:center}
/* footer */
.footer{left:0;top:3088px;width:1200px;height:344px;background:linear-gradient(90deg,#0b0b0b 0%,#1b1c1f 50%,#0f0f10 100%)}
.foot-col h5{font-size:16.5px;letter-spacing:.5px}
.foot-col ul{list-style:none;margin-top:18px;font-size:12.5px;line-height:23.5px}
.social{top:3285px;width:26px;height:26px;border:1.3px solid #ddd;border-radius:50%}
</style>
</head>
<body>

<!-- Header -->
<div class="abs brand" style="left:169px;top:28px"><i></i>Sunline Tint</div>
<nav class="abs nav">
  <a style="left:0;font-weight:700">Home</a>
  <a style="left:84px">Vehicle Wraps</a>
  <a style="left:212px">Commercial Wraps</a>
  <a style="left:366px">Portfolio</a>
  <a style="left:461px">Contact Us</a>
</nav>
<div class="abs call">
  <svg width="34" height="34" viewBox="0 0 34 34" fill="none" stroke="#fff" stroke-width="2"><circle cx="17" cy="17" r="13"/><path d="M9 11c1-2 3-2 4 0l1 2-2 2c1 2 3 4 5 5l2-2 2 1c2 1 2 3 0 4-4 2-13-7-12-12z" fill="#fff" stroke="none"/><text x="15" y="20" font-size="9" font-family="Arial" font-weight="700" fill="#fff" stroke="none">24</text></svg>
</div>

<!-- Hero -->
<div class="abs hero-photo" role="img" aria-label="Technician smiling while applying tint film to a car window"></div>
<div class="abs eyebrow"><span></span>COMMERCIAL &amp; RESIDENTIAL WINDOW TINTING</div>
<h1 class="abs serif hero-title">Tint your car window<br>to the next level</h1>
<p class="abs hero-text">Lorem ipsum dolor sit amet, consectetur adipisicing elit, sed do eiusmod tempor incididunt ut labore et dolore magna aliqua. Ut enim ad minim veniam, quis nostrud exercitation ullamco laboris nisi.</p>
<div class="abs btn-red">DISCOVER MORE</div>
<div class="abs ghost" style="left:-6px;top:462px;font-size:120px">DOW</div>

<!-- Stats -->
<div class="abs stat-num" style="left:168px">8K+</div>
<div class="abs stat-num" style="left:388px">22+</div>
<div class="abs stat-num" style="left:612px;color:var(--red)">500+</div>
<div class="abs stat-num" style="left:833px">99%</div>
<div class="abs" style="left:169px;top:658px;width:861px;height:1px;background:var(--rule)"></div>
<div class="abs" style="left:613px;top:657px;width:93px;height:3px;background:var(--red)"></div>
<div class="abs stat-label" style="left:169px">Happy Client fermentum<br>iaculis diam phasellus</div>
<div class="abs stat-label" style="left:389px">Happy Client fermentum<br>iaculis diam phasellus</div>
<div class="abs stat-label" style="left:613px;color:var(--white)">Happy Client fermentum<br>iaculis diam phasellus</div>
<div class="abs stat-label" style="left:834px">Happy Client fermentum<br>iaculis diam phasellus</div>

<!-- Services -->
<div class="abs card" style="left:169px;top:799px">
  <div class="photo" role="img" aria-label="Hand wiping a tinted car window with a cloth" style="background:linear-gradient(135deg,#4a4a4e,#25262a 60%,#101012)"></div>
  <div class="shade"></div>
  <h3 class="serif">Window Tinting</h3>
  <p>Happy Client fermentum iaculis diam phasellus vestibulum lorem eget mauris pharetra et.</p>
  <div class="more">Read More →</div>
</div>
<div class="abs card" style="left:610px;top:799px">
  <div class="photo" role="img" aria-label="Installers stretching vinyl wrap over a car body" style="background:linear-gradient(135deg,#8a8680,#4b4d52 55%,#1b1c20)"></div>
  <div class="shade"></div>
  <h3 class="serif">Vehicle Vinyl Wraps</h3>
  <p>Happy Client fermentum iaculis diam phasellus vestibulum lorem eget mauris pharetra et.</p>
  <div class="more">Read More →</div>
</div>
<div class="abs card" style="left:169px;top:1154px">
  <div class="photo" role="img" aria-label="Gloved hand applying protection film to a red car with a squeegee" style="background:linear-gradient(160deg,#7a1c22,#3b1216 50%,#141012)"></div>
  <div class="shade"></div>
  <h3 class="serif">Paint Protection Film</h3>
  <p>Happy Client fermentum iaculis diam phasellus vestibulum lorem eget mauris pharetra et.</p>
  <div class="more">Read More →</div>
</div>
<div class="abs card" style="left:610px;top:1154px">
  <div class="photo" role="img" aria-label="Technician in a cap working on a car windshield" style="background:linear-gradient(135deg,#9a9a9c,#4d5560 50%,#15181c)"></div>
  <div class="shade"></div>
  <h3 class="serif">Windshield Protection</h3>
  <p>Happy Client fermentum iaculis diam phasellus vestibulum lorem eget mauris pharetra et.</p>
  <div class="more">Read More →</div>
</div>

<!-- Video -->
<div class="abs ghost" style="left:746px;top:1492px;font-size:118px">TINTING</div>
<h2 class="abs serif section-title" style="left:169px;top:1558px">Car Window Tinting</h2>
<div class="abs" style="left:169px;top:1613px;width:862px;height:1px;background:var(--rule)"></div>
<div class="abs video" role="img" aria-label="Video still of a technician applying tint film to a car door window"></div>
<div class="abs play"><svg width="26" height="28" viewBox="0 0 26 28"><path d="M2 1l23 13L2 27z" fill="#fff"/></svg></div>

<!-- Why us -->
<div class="abs frame"></div>
<div class="abs feat-photo" role="img" aria-label="Low angle view of a red car wheel in a bright garage"></div>

<div class="abs feat" style="left:627px;top:2213px">
  <div class="icon"><svg width="28" height="28" viewBox="0 0 28 28" fill="none" stroke="#fff" stroke-width="2"><circle cx="10" cy="9" r="4"/><circle cx="19" cy="9" r="4"/><path d="M3 24c0-5 3-8 7-8s7 3 7 8M12 24c0-5 3-8 7-8s6 3 6 8"/></svg></div>
  <div class="num">01</div>
  <h4 class="serif">Dedicated Team</h4>
  <p>Lorem ipsum dolor sit amet, consectetur adipisicing elit, sed do eiusmod tempor incididunt ut labore,</p>
</div>
<div class="abs feat" style="left:848px;top:2178px">
  <div class="icon"><svg width="26" height="28" viewBox="0 0 26 28" fill="none" stroke="#fff" stroke-width="2"><path d="M13 26s-8-8-8-14a8 8 0 0116 0c0 6-8 14-8 14z"/><circle cx="13" cy="12" r="3"/></svg></div>
  <div class="num">02</div>
  <h4 class="serif">Locally Owned</h4>
  <p>Lorem ipsum dolor sit amet, consectetur adipisicing elit, sed do eiusmod tempor incididunt ut labore,</p>
</div>
<div class="abs feat" style="left:627px;top:2442px">
  <div class="icon"><svg width="24" height="28" viewBox="0 0 24 28" fill="none" stroke="#fff" stroke-width="2"><path d="M12 2a8 8 0 00-5 14v4h10v-4a8 8 0 00-5-14zM8 24h8"/></svg></div>
  <div class="num">03</div>
  <h4 class="serif">Knowledgeable</h4>
  <p>Lorem ipsum dolor sit amet, consectetur adipisicing elit, sed do eiusmod tempor incididunt ut labore,</p>
</div>
<div class="abs feat" style="left:848px;top:2406px">
  <div class="icon"><svg width="26" height="26" viewBox="0 0 26 26" fill="none" stroke="#fff" stroke-width="2.2"><path d="M5 14l5 5L21 7"/></svg></div>
  <div class="num">04</div>
  <h4 class="serif">Competitive</h4>
  <p>Lorem ipsum dolor sit amet, consectetur adipisicing elit, sed do eiusmod tempor incididunt ut labore,</p>
</div>

<!-- Reviews -->
<h2 class="abs serif section-title" style="left:169px;top:2812px">Our Customer Reviews</h2>
<p class="abs" style="left:169px;top:2866px;width:370px;font-size:11.5px;line-height:21px;letter-spacing:.6px;color:var(--muted)">Lorem ipsum dolor sit amet, consectetur adipisicing elit, sed do eiusmod tempor incididunt ut labore,et dolore magna aliqua. Ut enim ad minim veniam,</p>
<div class="abs btn-line">VIEW ALL</div>

<div class="abs review-card">
  <div class="abs" style="left:35px;top:38px;color:var(--gold);font-size:15px;letter-spacing:4px">★★★★★</div>
  <p class="abs" style="left:35px;top:80px;width:330px;font-size:11.5px;line-height:21px;letter-spacing:.5px">"Lorem ipsum dolor sit amet, consectetur adipisicing elit, sed do eiusmod tempor incididunt ut labore et dolore magna aliqua. Ut enim ad minim veniam, quis nostrud exercitation ullamco laboris nisi ut aliquip ex ea commodo consequat".</p>
  <div class="abs serif" style="left:35px;top:202px;font-size:15px;text-transform:none">Dara Whitlow</div>
  <div class="abs" style="left:35px;top:224px;font-size:10px;color:var(--muted)">CEO</div>
  <svg class="abs" style="left:325px;top:198px" width="40" height="32" viewBox="0 0 40 32" fill="none" stroke="var(--gold)" stroke-width="2"><circle cx="9" cy="9" r="7"/><path d="M16 9c0 10-6 18-14 20"/><circle cx="29" cy="9" r="7"/><path d="M36 9c0 10-6 18-14 20"/></svg>
</div>

<!-- Footer -->
<div class="abs footer" role="img" aria-label="Dim background of a car in a workshop"></div>
<div class="abs brand" style="left:155px;top:3198px"><i></i>Sunline Tint</div>
<div class="abs social" style="left:152px"></div>
<div class="abs social" style="left:187px"></div>
<div class="abs social" style="left:221px"></div>

<div class="abs foot-col" style="left:381px;top:3162px">
  <h5 class="serif">Useful Link</h5>
  <ul><li>Home</li><li>Vehicle Wraps</li><li>Commercial Wraps</li><li>Ppf</li><li>Contact Us</li></ul>
</div>
<div class="abs foot-col" style="left:610px;top:3162px">
  <h5 class="serif">Services</h5>
  <ul><li>Window Tinting</li><li>Vehicle Vinyl Wraps</li><li>Paint Film</li><li>Windshield Protection</li><li>Try &amp; Wheels</li></ul>
</div>
<div class="abs foot-col" style="left:837px;top:3162px">
  <h5 class="serif">Contact Us</h5>
  <ul><li>Call us on:</li><li>+1 (209) 555-0148</li><li style="margin-top:12px">Email Us on:</li><li>hello@sunlinetint.com</li></ul>
</div>

<div class="abs" style="left:152px;top:3366px;width:893px;height:1px;background:var(--rule)"></div>
<div class="abs" style="left:152px;top:3390px;font-size:12px">© Copyright 2023 Sunline Tint. All right reserved.</div>
<div class="abs" style="left:955px;top:3390px;font-size:12px">Privacy &amp; Policy</div>

</body>
</html>
```